Quarry Provision Partners needs a cool web design

We need a web design for a new start up called Quarry Provision Partners. QPP is all about working with mine sites to reduce costs and make their supply chains more effective and cost efficient. I have attached our logo and a very basic tile format layout for the website but I will take your advice on best layout. I do prefer a tile based page similar to "Farvenbrook.com/advisory" this displays a professional yet cool look. The secondary pages need to have the same format.
Target Market(s)
Target customers are typically men in the mining industry. They want simplicity and are time poor.
Industry/Entity Type
Mining
Coding
Coded - Design and coding required
Font styles to use
Requirements
Must have
- Must be simple, prefer tile based such as the Farvenbrooks.com/advisory website.
Use bold writing and fonts. No flowery fonts.
Must use corporate colors but don't make too dark.
the site must have connections to well designed second pages.

```html
<!DOCTYPE html>
<html lang="en">
<head>
<meta charset="utf-8">
<title>Quarry Provision Partners</title>
<link href="https://fonts.googleapis.com/css2?family=Raleway:wght@500;600;700&family=Open+Sans:wght@400;600&display=swap" rel="stylesheet">
<style>
:root{
  --black:#000;
  --red:#d8141f;
  --tile-red:#a30a18;
  --tile-dark:#1d1d1d;
  --tile-maroon:#3d1719;
  --white:#fff;
  --muted:#b9b9b9;
  --grey:#d6d6d6;
  --footer:#e1e1e1;
  --ink:#2a2a2a;
}
*{margin:0;padding:0;box-sizing:border-box}
html,body{width:1200px;height:890px;overflow:hidden;background:#fff;font-family:"Open Sans",sans-serif}
.page{position:relative;width:1200px;height:890px}
.site-header{position:absolute;left:0;top:0;width:1200px;height:101px;background:var(--black)}
.brand{position:absolute;left:192px;top:27px;display:flex;align-items:center;gap:10px}
.brand-mark{width:44px;height:44px;background:var(--red)}
.brand-name{font-family:"Raleway",sans-serif;font-weight:700;color:var(--white);font-size:14px;line-height:17px;letter-spacing:.5px;text-transform:uppercase}
.main-nav{position:absolute;top:0;left:620px;height:101px;display:flex}
.main-nav a{display:flex;align-items:center;justify-content:center;height:101px;color:var(--white);text-decoration:none;font-family:"Raleway",sans-serif;font-weight:600;font-size:13px;border-right:1px solid #2b2b2b}
.main-nav a.active{color:var(--red)}
.main-nav a:last-child{border-right:none}
.service-tile{position:absolute;left:190px;width:208px;height:105px;padding:18px 26px;color:var(--white)}
.service-tile.dark{background:linear-gradient(#2c2c2c,#121212)}
.service-tile.red{background:var(--tile-red)}
.service-tile.maroon{background:var(--tile-maroon)}
.service-tile h3{font-family:"Raleway",sans-serif;font-weight:500;font-size:16px;line-height:20px}
.service-tile h3 small{display:block;font-size:12.5px;line-height:20px;font-weight:500}
.service-tile p{font-size:9px;line-height:13px;color:var(--muted);margin-top:5px;width:130px}
.service-tile.red p{color:#e29aa0}
.service-tile svg{position:absolute;right:20px;top:22px}
.hero{position:absolute;left:405px;top:119px;width:608px;height:292px;background:linear-gradient(#5b5d60,#7d7f82 45%,#3a3b3d)}
.hero-caption{position:absolute;left:9px;top:139px;width:303px;height:90px;background:rgba(235,235,235,.82);padding:19px 24px}
.hero-caption .kicker{font-family:"Raleway",sans-serif;font-weight:600;color:var(--red);font-size:19px;line-height:22px}
.hero-caption .title{font-family:"Raleway",sans-serif;font-weight:700;color:#111;font-size:22px;line-height:28px}
.dots{position:absolute;top:267px;left:262px;display:flex;gap:4px}
.dots span{width:12px;height:12px;border-radius:50%;background:#fff}
.dots span:first-child{background:#000}
.welcome{position:absolute;left:405px;top:418px;width:608px;height:184px;background:linear-gradient(100deg,#2c2119,#4a3526 55%,#33261c);padding:28px 27px;color:var(--white)}
.welcome h1{font-family:"Raleway",sans-serif;font-weight:500;font-size:19px;line-height:22px}
.welcome h1 .accent{color:var(--red)}
.welcome h1 big{display:block;font-size:24px;line-height:30px}
.welcome p{font-size:9.2px;line-height:15.5px;margin-top:6px;color:#eee}
.case-studies{position:absolute;left:406px;top:611px;width:298px;height:175px;background:var(--grey);padding:25px 27px;color:var(--ink)}
.case-studies h2,.global h2{font-family:"Raleway",sans-serif;font-weight:500;font-size:19px;line-height:24px}
.case-studies p{font-size:9.2px;line-height:15.5px;margin-top:6px}
.byline{font-family:"Raleway",sans-serif;font-weight:600;font-size:11.5px;margin-top:6px}
.global{position:absolute;left:714px;top:611px;width:299px;height:175px;background:linear-gradient(135deg,#3a3430,#595048 60%,#2e2a27);padding:25px 27px;color:var(--white)}
.global p{font-size:9.2px;line-height:15.5px;margin-top:6px;width:140px}
.global .learn{font-family:"Raleway",sans-serif;font-weight:600;font-size:11.5px;margin-top:5px}
.global-photo{position:absolute;left:169px;top:59px;width:116px;height:80px;background:linear-gradient(#6d93c2,#b9785a 55%,#c15a2c)}
.site-footer{position:absolute;left:0;top:820px;width:1200px;height:70px;background:var(--footer)}
.site-footer p{position:absolute;left:191px;top:22px;font-size:10px;color:#333}
.social{position:absolute;left:946px;top:18px;display:flex;gap:5px}
.social span{width:17px;height:17px;border-radius:3px;background:#1f5b9e}
</style>
</head>
<body>
<div class="page">
  <header class="site-header">
    <div class="brand">
      <div class="brand-mark"></div>
      <div class="brand-name">Quarry<br>Provision<br>Partners</div>
    </div>
    <nav class="main-nav">
      <a class="active" href="#" style="width:84px">HOME</a>
      <a href="#" style="width:92px">ABOUT</a>
      <a href="#" style="width:108px">SERVICES</a>
      <a href="#" style="width:110px">CONTACT</a>
    </nav>
  </header>

  <a class="service-tile dark" style="top:119px">
    <h3>Procurement<br>Services</h3>
    <p>Lorem ipsum dolor sit amet conse ctetuer adipis</p>
    <svg width="40" height="30" viewBox="0 0 40 30" fill="none" stroke="#fff" stroke-width="2.5"><path d="M2 6l8 2 4 12h16l6-12H10"/><circle cx="27" cy="25" r="4"/></svg>
  </a>
  <a class="service-tile red" style="top:231px">
    <h3>Strategic<small>Sourcing Services</small></h3>
    <p>Lorem ipsum dolor sit amet conse ctetuer</p>
    <svg width="36" height="32" viewBox="0 0 36 32" fill="#fff"><rect x="2" y="18" width="5" height="14"/><rect x="10" y="14" width="5" height="18"/><rect x="18" y="12" width="5" height="20"/><rect x="26" y="8" width="5" height="24"/><path d="M2 14l10-6 6 3 12-9" stroke="#fff" stroke-width="2.5" fill="none"/></svg>
  </a>
  <a class="service-tile dark" style="top:342px">
    <h3>Lead Time<small>Reduction Services</small></h3>
    <p>Lorem ipsum dolor sit amet conse ctetuer adipis</p>
    <svg width="32" height="32" viewBox="0 0 32 32" fill="none" stroke="#fff" stroke-width="3"><circle cx="16" cy="16" r="13.5"/><path d="M16 8v8l6 4"/></svg>
  </a>
  <a class="service-tile red" style="top:454px">
    <h3>Inventory<small style="font-size:14px">Optimisation<br>Services</small></h3>
    <p>Lorem ipsum dolor sit amet</p>
    <svg width="36" height="30" viewBox="0 0 36 30" fill="#fff"><path d="M2 6l16-5 16 5-6 4H8z"/><path d="M5 12h26v16H5z"/><rect x="16" y="10" width="4" height="18" fill="#a30a18"/></svg>
  </a>
  <a class="service-tile maroon" style="top:566px">
    <h3>Critical Spare<br>Parts Audit</h3>
    <p>Lorem ipsum dolor sit amet conse ctetuer adipiscing elit Nam</p>
    <svg width="32" height="32" viewBox="0 0 32 32" fill="#fff"><path d="M2 3h28v4H2z"/><path d="M4 8h24l-3 14H7z"/><circle cx="9" cy="27" r="4"/><circle cx="23" cy="27" r="4"/></svg>
  </a>
  <a class="service-tile dark" style="top:678px">
    <h3>Supply Chain<small style="font-size:14px">Health Check</small></h3>
    <p>Lorem ipsum dolor sit amet conse ctetuer adipiscing elit Nam</p>
    <svg width="30" height="30" viewBox="0 0 30 30"><circle cx="15" cy="15" r="14" fill="#fff"/><path d="M8 6c4 2 2 6 6 7s1 6-3 8M20 4c-2 4 3 5 6 4M19 18c3 0 5 2 4 6" stroke="#1d1d1d" stroke-width="3" fill="none"/></svg>
  </a>

  <section class="hero" role="img" aria-label="Photo of yellow mine haul trucks on a grey gravel quarry road">
    <div class="hero-caption">
      <div class="kicker">MORBI DIAM MAURIS</div>
      <div class="title">CUM SOCIIS NATOQUE</div>
    </div>
    <div class="dots"><span></span><span></span><span></span></div>
  </section>

  <section class="welcome" role="img" aria-label="Dark brown background photo of mining machinery">
    <h1><span class="accent">WELCOME TO</span> QUARRY<big>PROVISION PARTNERS</big></h1>
    <p>Vivamus porttitor purus nisi eleifend libero a tempus libero lectus feugiat felis Morbi diam mauris viverra in gravida eu mattis in ante Morbi eget arcu Morbi porta libero id ullamcorper nonummy nibh ligula pulvinar metus eget consectetuer augue nisi quis lacus Ut ac mi quis lacus mollis aliquam Curabitur iaculis tempus eros<br>Curabitur vel mi sit amet magna malesuada ultrices Ut nisi erat fermentum vel congue id euismod in elit Fuscev</p>
  </section>

  <section class="case-studies">
    <h2>Case Studies</h2>
    <p>ro a tempus libero lectus feugiat felis Morbi diam mauris viverra in gravida eu mattis in ante Morbi eget arcu Morbi porta libero id ullamcorper nonummy nibh ligula pulvinar metus eget consectetuer augue nisi quis lacus Ut ac mi quis lacus mollis</p>
    <div class="byline">By Author Name</div>
  </section>

  <section class="global" role="img" aria-label="Background photo of a terraced open-pit mine">
    <h2>Global Presence</h2>
    <p>Ao a tempus libero lectus feugiat felis Morbi diam mauris viverra in gravida eu mattis in ante Morbi eget arcu Morbi porta libero</p>
    <div class="learn">Learn More</div>
    <div class="global-photo" role="img" aria-label="Photo of mining trucks on red earth under a blue sky"></div>
  </section>

  <footer class="site-footer">
    <p>© 2015 Company Name &nbsp;All right reserved &nbsp;Term of Use</p>
    <div class="social"><span></span><span></span><span></span></div>
  </footer>
</div>
</body>
</html>
```